Business Card Design Project - Photographer

Photography business needs a logo. I would like to see creative licence on options on 1 & 2 sided. I really like the concept of a fully / partially frosted design. I have already used ArtHive for my Logo, so I am looking for the same level of assistance with this project.

If you have any questions please let me know

Cheers Morris

Industry/Entity Type

Business

Requirements
Must have
• These are my contact details
Name: Morris Tilbury
Mobile: 0438 216 907
email: morris@brightlensstudio.com.au
Website: www.brightlensstudio.com.au
Nice to have
• Facebook: https://www.facebook.com/BrightLensStudioAus

```html
<!DOCTYPE html>
<html lang="en">
<head>
<meta charset="utf-8">
<title>BrightLens Studio – Business Card</title>
<link rel="stylesheet" href="https://fonts.googleapis.com/css2?family=Quicksand:wght@500;600&display=swap">
<style>
  :root {
    --card-bg: #ffffff;
    --ink: #1c1c1c;
    --accent-red: #c4161c;
    --mark-red: #d0171f;
  }
  * { margin: 0; padding: 0; box-sizing: border-box; }
  html, body {
    width: 702px;
    height: 1200px;
    overflow: hidden;
    background: var(--card-bg);
  }
  .card {
    position: relative;
    width: 702px;
    height: 1200px;
    background: var(--card-bg);
    font-family: "Quicksand", sans-serif;
    color: var(--ink);
  }
  .brand {
    position: absolute;
    top: 150px;
    left: 0;
    width: 100%;
    display: flex;
    flex-direction: column;
    align-items: center;
  }
  .brand-dot {
    width: 200px;
    height: 200px;
    border-radius: 50%;
    background: var(--mark-red);
  }
  .brand-name {
    margin-top: 50px;
    text-align: center;
    font-weight: 600;
    color: var(--ink);
    line-height: 1;
  }
  .brand-name .primary {
    display: block;
    font-size: 78px;
    letter-spacing: 0.02em;
  }
  .brand-name .secondary {
    display: block;
    margin-top: 22px;
    font-size: 30px;
    letter-spacing: 0.62em;
    padding-left: 0.62em;
  }
  .contact {
    position: absolute;
    left: 61px;
    top: 976px;
    list-style: none;
    font-weight: 500;
    font-size: 22px;
    line-height: 27.5px;
    text-transform: uppercase;
    letter-spacing: 0.02em;
  }
  .contact .label { color: var(--accent-red); }
  .contact .value { color: var(--ink); }
</style>
</head>
<body>
  <main class="card">
    <header class="brand">
      <div class="brand-dot" aria-hidden="true"></div>
      <h1 class="brand-name">
        <span class="primary">BRIGHTLENS</span>
        <span class="secondary">STUDIO</span>
      </h1>
    </header>

    <ul class="contact">
      <li><span class="label">Name:</span> <span class="value">Morris Tilbury</span></li>
      <li><span class="label">Mobile:</span> <span class="value">0438 216 907</span></li>
      <li><span class="label">Email:</span> <span class="value">morris@brightlensstudio.com.au</span></li>
      <li><span class="label">Website:</span> <span class="value">www.brightlensstudio.com.au</span></li>
    </ul>
  </main>
</body>
</html>
```